Web Design Business Card

I need a new business card designed, we recently rebranded and I need to get a fresh design to match our new logo, colours and branding.

Details:

Dorian Keeble | Founder & CEO
Address: 7 Fernhollow Lane, #04-09 Maplecrest Vale, Singapore 583104
Tel: +65 93468120
Web: www.plumtrove.com.sg
hello@plumtrove.com.sg

I've attached my old card as well

Requirements
Must have
• Front and Back
Interesting use of logo
Correct use of colour scheme

```html
<!DOCTYPE html>
<html lang="en">
<head>
<meta charset="utf-8">
<title>Plumtrove Business Card</title>
<link rel="stylesheet" href="https://fonts.googleapis.com/css2?family=Questrial&display=swap">
<style>
  :root {
    --backdrop: #e9e6e3;
    --card-top: #ffffff;
    --card-bottom: #e6e6e6;
    --brand-blue: #2f9fd4;
    --brand-blue-light: #48b2e0;
    --ink-brown: #5b4a42;
    --shadow: rgba(40, 28, 20, 0.22);
  }
  * { margin: 0; padding: 0; box-sizing: border-box; }
  html, body {
    width: 1200px;
    height: 900px;
    overflow: hidden;
    background: var(--backdrop);
    font-family: "Questrial", "Century Gothic", sans-serif;
  }
  .canvas {
    position: relative;
    width: 1200px;
    height: 900px;
  }
  .card {
    position: absolute;
    width: 560px;
    height: 320px;
    border-radius: 22px;
    background: linear-gradient(160deg, var(--card-top) 0%, #f6f6f6 55%, var(--card-bottom) 100%);
    box-shadow: 0 10px 26px var(--shadow), 0 2px 4px rgba(0,0,0,0.12);
    overflow: hidden;
  }

  /* Back of the card: blank field with brand lockup bottom-left */
  .card--back { left: 90px; top: 110px; }
  .lockup {
    position: absolute;
    left: 32px;
    bottom: 30px;
    display: flex;
    align-items: center;
    gap: 12px;
  }
  .lockup__dot {
    width: 44px;
    height: 44px;
    border-radius: 50%;
    background: var(--brand-blue);
  }
  .lockup__text { display: flex; flex-direction: column; }
  .lockup__name {
    font-size: 30px;
    line-height: 1;
    color: var(--ink-brown);
    letter-spacing: 0.2px;
  }
  .lockup__tagline {
    margin-top: 4px;
    font-size: 8px;
    letter-spacing: 1.4px;
    color: var(--brand-blue);
    text-transform: uppercase;
  }

  /* Front of the card: contact details */
  .card--front { left: 550px; top: 470px; }
  .brand-mark {
    position: absolute;
    right: 40px;
    top: 26px;
    display: flex;
    flex-direction: column;
    align-items: center;
    gap: 8px;
  }
  .brand-mark__circle {
    width: 150px;
    height: 150px;
    border-radius: 50%;
    background: linear-gradient(180deg, var(--brand-blue) 0%, var(--brand-blue-light) 100%);
  }
  .brand-mark__name {
    font-size: 18px;
    color: var(--ink-brown);
  }
  .person {
    position: absolute;
    left: 44px;
    top: 92px;
  }
  .person__name {
    font-size: 26px;
    color: var(--ink-brown);
    font-weight: 400;
  }
  .person__role {
    margin-top: 6px;
    margin-left: 34px;
    font-size: 14px;
    color: var(--brand-blue);
  }
  .contact {
    position: absolute;
    left: 44px;
    top: 200px;
    list-style: none;
    font-size: 15px;
    color: var(--ink-brown);
  }
  .contact li { margin-bottom: 10px; }
  .contact__label { color: var(--brand-blue); margin-right: 4px; }
  .address {
    position: absolute;
    left: 130px;
    bottom: 22px;
    font-size: 14px;
    color: var(--ink-brown);
    font-style: normal;
  }
</style>
</head>
<body>
  <main class="canvas">
    <section class="card card--back" aria-label="Card back">
      <div class="lockup">
        <span class="lockup__dot"></span>
        <div class="lockup__text">
          <span class="lockup__name">plumtrove</span>
          <span class="lockup__tagline">Web Design &amp; Consultancy</span>
        </div>
      </div>
    </section>

    <section class="card card--front" aria-label="Card front">
      <div class="brand-mark">
        <span class="brand-mark__circle"></span>
        <span class="brand-mark__name">plumtrove</span>
      </div>

      <div class="person">
        <h1 class="person__name">Dorian Keeble</h1>
        <p class="person__role">Founder &amp; CEO</p>
      </div>

      <ul class="contact">
        <li><span class="contact__label">T:</span> +65 93468120</li>
        <li><span class="contact__label">W:</span> www.plumtrove.com.sg</li>
        <li><span class="contact__label">E:</span> hello@plumtrove.com.sg</li>
      </ul>

      <address class="address">7 Fernhollow Lane, #04-09 Maplecrest Vale Singapore 583104</address>
    </section>
  </main>
</body>
</html>
```